ZEH Project Signage

Need a sign to be displayed in the front of properties currently under Construction or Renovation to advertise our company information. Need it to be Professional and Contemporary. We are a Design/Build Construction Company. Information should include Company Name, email, website, phone number. Attached: Logo and company brochure, also included and inspiration images

```html
<!DOCTYPE html>
<html lang="en">
<head>
<meta charset="utf-8">
<title>ZEH Construction – Project Sign</title>
<link href="https://fonts.googleapis.com/css2?family=Poppins:wght@500;600;700&display=swap" rel="stylesheet">
<style>
  :root {
    --backdrop: #5f5f5f;
    --paper: #ffffff;
    --ink: #111111;
    --night: #0b0b0b;
    --night-soft: #1a1a1a;
    --accent: #f2e94a;
    --icon: #bdbdbd;
    --light: #ffffff;
  }
  * { margin: 0; padding: 0; box-sizing: border-box; }
  html, body { width: 829px; height: 1200px; overflow: hidden; }
  body {
    background: var(--backdrop);
    font-family: "Poppins", sans-serif;
    position: relative;
  }
  .sign {
    position: absolute;
    left: 86px; top: 107px;
    width: 658px; height: 986px;
    background: var(--paper);
    box-shadow: 0 6px 22px rgba(0,0,0,0.45);
    overflow: hidden;
  }
  .brand {
    position: absolute; left: 0; top: 100px; width: 100%;
    display: flex; justify-content: center; align-items: center; gap: 14px;
  }
  .brand-dot {
    width: 30px; height: 30px; border-radius: 50%;
    background: var(--accent);
  }
  .brand-name {
    font-weight: 600; font-size: 40px; letter-spacing: 1px;
    color: var(--ink); line-height: 1;
  }
  .tagline {
    position: absolute; left: 0; top: 178px; width: 100%;
    text-align: center; font-weight: 500; font-size: 24px;
    letter-spacing: 1.5px; color: var(--ink);
  }
  .site-small {
    position: absolute; left: 0; top: 222px; width: 100%;
    text-align: center; font-weight: 600; font-size: 20px; color: var(--ink);
  }
  .contact-band {
    position: absolute; left: 0; top: 350px; width: 100%; height: 526px;
    background: radial-gradient(ellipse at 50% 45%, var(--night-soft), var(--night) 75%);
  }
  .service-pill {
    position: absolute; left: 129px; top: 328px; width: 400px; height: 68px;
    background: #000; border: 2px solid var(--light); border-radius: 14px;
    display: flex; align-items: center; justify-content: center;
    color: var(--light); font-weight: 700; font-size: 42px; letter-spacing: 0.5px;
  }
  .icon { position: absolute; left: 50%; transform: translateX(-50%); }
  .icon-phone { top: 434px; }
  .icon-mail { top: 568px; }
  .icon-pin { top: 680px; }
  .line {
    position: absolute; left: 0; width: 100%; text-align: center;
    color: var(--light); line-height: 1;
  }
  .phone { top: 487px; font-weight: 700; font-size: 46px; }
  .email { top: 622px; font-weight: 500; font-size: 29px; }
  .address {
    position: absolute; left: 0; top: 736px; width: 100%;
    text-align: center; color: var(--light);
    font-weight: 600; font-size: 27px; line-height: 37px;
  }
  .site-large {
    position: absolute; left: 0; top: 906px; width: 100%;
    text-align: center; font-weight: 700; font-size: 36px; color: var(--ink);
  }
</style>
</head>
<body>
  <main class="sign">
    <div class="brand">
      <span class="brand-dot"></span>
      <span class="brand-name">ZEH CONSTRUCTION</span>
    </div>
    <p class="tagline">LUXURY RENOVATIONS</p>
    <p class="site-small">www.zehconstruction.com</p>

    <section class="contact-band" role="img" aria-label="Dark, dimmed photo of a finished luxury interior behind the contact details"></section>

    <div class="service-pill">DESIGN-BUILD</div>

    <svg class="icon icon-phone" width="46" height="46" viewBox="0 0 24 24" aria-hidden="true">
      <path fill="var(--icon)" d="M6.6 2.5c.6-.4 1.4-.2 1.8.4l2 3.1c.4.6.3 1.3-.2 1.8l-1.3 1.2c.9 2 2.4 3.6 4.3 4.6l1.3-1.2c.5-.5 1.3-.5 1.8-.1l3 2.2c.6.4.7 1.3.2 1.9l-1.3 1.6c-.8.9-2.1 1.3-3.3.9C9.6 17.6 5.6 13.4 4.3 8.2c-.3-1.2.1-2.4 1-3.2z"/>
      <path fill="none" stroke="var(--icon)" stroke-width="1.5" stroke-linecap="round" d="M14 6.2a4 4 0 0 1 3.8 3.8M14.2 2.6a7.6 7.6 0 0 1 7.2 7.2"/>
    </svg>
    <p class="line phone">561.555.0148</p>

    <svg class="icon icon-mail" width="48" height="46" viewBox="0 0 48 46" aria-hidden="true">
      <rect x="10" y="2" width="28" height="24" fill="var(--icon)"/>
      <text x="24" y="20" text-anchor="middle" font-family="Poppins, sans-serif" font-size="16" fill="#0b0b0b">@</text>
      <path fill="var(--icon)" d="M0 16 L24 32 L48 16 V46 H0 Z"/>
      <path fill="none" stroke="#0b0b0b" stroke-width="1.5" d="M1 45 L19 29 M47 45 L29 29"/>
    </svg>
    <p class="line email">info@zehconstruction.com</p>

    <svg class="icon icon-pin" width="48" height="48" viewBox="0 0 48 48" aria-hidden="true">
      <ellipse cx="24" cy="40" rx="22" ry="7" fill="none" stroke="var(--icon)" stroke-width="3"/>
      <path fill="var(--icon)" d="M24 2a13 13 0 0 0-13 13c0 9 13 25 13 25s13-16 13-25A13 13 0 0 0 24 2z"/>
      <circle cx="24" cy="15" r="4" fill="#0b0b0b"/>
    </svg>
    <p class="address">1450 Harbor View Ave.<br>Suite 310<br>Coral Point, FL 33400</p>

    <p class="site-large">www.zehconstruction.com</p>
  </main>
</body>
</html>
```